Power Point Template Design for Consulting Company
Verdant Ridge Inc.
Helping Clients Achieve Explosive Sales
Need a slide master incorporating existing logo for all regular Power Point slide layout types (title, title and content, section header, two content, comparison, title only, blank, content with caption, picture with caption)
Corporate client presentations and professional association speaking engagements
Using Power Point 2007, Windows 7.0 O/S.
Not overpowering, prefer clean white backgrounds for better projection and printing results. Verdant Ridge Inc. Logo was designed on a previous project so all files available.
logo files in all formats
business card for reference and consistency
business letterhead for reference and consistency
business stationary coor and font for reference and consistency

```html
<!DOCTYPE html>
<html lang="en">
<head>
<meta charset="utf-8">
<title>Verdant Ridge Inc. – Slide Master Set</title>
<link href="https://fonts.googleapis.com/css2?family=Arimo:wght@400;700&display=swap" rel="stylesheet">
<style>
  :root {
    --board: #7b7c7e;
    --paper: #ffffff;
    --paper-shade: #e4e6ea;
    --blue-deep: #0b3f86;
    --blue-mid: #1565b8;
    --blue-light: #3b8fdc;
    --blue-pale: #8cc0ee;
    --ink-blue: #1f5fae;
    --ink-grey: #9a9ea4;
    --line: #c9ccd1;
    --white: #ffffff;
  }
  * { box-sizing: border-box; margin: 0; padding: 0; }
  html, body { width: 1200px; height: 725px; overflow: hidden; }
  body {
    background: var(--board);
    font-family: "Arimo", Arial, sans-serif;
    position: relative;
  }
  .slide {
    position: absolute;
    width: 245px;
    height: 207px;
    background:
      radial-gradient(ellipse at 100% 0%, var(--paper-shade) 0%, rgba(228,230,234,0.5) 35%, rgba(255,255,255,0) 65%),
      var(--paper);
    overflow: hidden;
    box-shadow: 0 1px 3px rgba(0,0,0,0.35);
  }
  .slide--blue {
    background:
      radial-gradient(ellipse at 20% 15%, var(--blue-light) 0%, rgba(59,143,220,0) 55%),
      linear-gradient(160deg, var(--blue-mid) 0%, var(--blue-deep) 75%);
  }
  .col1 { left: 34px; } .col2 { left: 329px; } .col3 { left: 622px; } .col4 { left: 919px; }
  .row1 { top: 34px; } .row2 { top: 264px; } .row3 { top: 492px; }

  .footer-band {
    position: absolute; left: 0; right: 0; bottom: 0; height: 20px;
    background: linear-gradient(90deg, var(--blue-deep), var(--blue-mid) 60%, var(--blue-light));
  }
  .footer-band::before, .footer-band::after {
    content: ""; position: absolute; top: 0; height: 7px; background: var(--blue-pale);
    transform: skewX(-35deg);
  }
  .footer-band::before { left: 18px; width: 40px; }
  .footer-band::after { left: 150px; width: 60px; opacity: 0.7; }
  .slide--blue .footer-band { background: linear-gradient(90deg, var(--blue-deep), var(--blue-mid)); opacity: 0.9; }

  .brand {
    position: absolute; display: flex; align-items: center; gap: 4px;
    font-size: 8px; font-weight: 700; color: var(--ink-blue); white-space: nowrap;
  }
  .brand__mark { width: 8px; height: 8px; background: var(--blue-mid); }
  .brand--small { left: 10px; top: 8px; }
  .brand--center { left: 0; right: 0; justify-content: center; font-size: 12px; gap: 6px; }
  .brand--center .brand__mark { width: 14px; height: 14px; }
  .slide--blue .brand { color: var(--white); }
  .slide--blue .brand__mark { background: var(--white); }

  .ph {
    position: absolute; border: 1px solid var(--line); background: rgba(255,255,255,0.6);
    font-size: 6px; color: var(--ink-grey); padding: 4px 5px;
  }
  .ph--title { font-size: 10px; font-weight: 700; color: var(--ink-blue); display: flex; align-items: center; }
  .ph--center { justify-content: center; text-align: center; display: flex; align-items: center; }
  .ph--sub { color: var(--ink-grey); font-size: 7px; }
  .slide--blue .ph { border-color: rgba(255,255,255,0.55); background: rgba(255,255,255,0.06); color: var(--white); }

  .photo-strip {
    position: absolute; left: 10px; right: 10px; top: 28px; height: 92px;
    background: linear-gradient(100deg, #4a4f57, #a6abb2 40%, #5a7fa8 70%, #d6d9de);
  }
  .tagline {
    position: absolute; left: 0; right: 0; top: 146px; text-align: center;
    font-size: 6.5px; color: var(--ink-grey);
  }
  .header-title { position: absolute; left: 22px; top: 32px; font-size: 13px; color: var(--ink-blue); }
  .bullets { position: absolute; left: 60px; top: 52px; list-style: none; font-size: 6px; color: var(--ink-grey); line-height: 10px; }
  .bullets li::before { content: "\2022 "; color: var(--blue-mid); }
  .divider-label { position: absolute; left: 70px; right: 70px; top: 102px; height: 22px; }
</style>
</head>
<body>

<!-- Row 1 -->
<section class="slide col1 row1" aria-label="Cover slide">
  <div class="brand brand--small"><span class="brand__mark"></span>Verdant Ridge Inc.</div>
  <div class="photo-strip" role="img" aria-label="Strip of business photographs"></div>
  <p class="tagline">Helping Clients Achieve Explosive Sales</p>
  <div class="footer-band"></div>
</section>

<section class="slide slide--blue col2 row1" aria-label="Title slide, blue">
  <div class="brand brand--center" style="top:30px"><span class="brand__mark"></span>Verdant Ridge Inc.</div>
  <div class="ph ph--title ph--center" style="left:40px;right:40px;top:64px;height:28px;color:var(--white)">Click to add Title</div>
  <div class="ph ph--sub ph--center" style="left:50px;right:50px;top:104px;height:22px">Click to add Subtitle</div>
</section>

<section class="slide col3 row1" aria-label="Title slide">
  <div class="brand brand--small"><span class="brand__mark"></span>Verdant Ridge Inc.</div>
  <div class="ph ph--title ph--center" style="left:40px;right:40px;top:52px;height:32px">Click to add Title</div>
  <div class="ph ph--sub ph--center" style="left:50px;right:50px;top:102px;height:22px">Click to add Subtitle</div>
  <div class="footer-band"></div>
</section>

<section class="slide col4 row1" aria-label="Section header slide">
  <div class="brand brand--small"><span class="brand__mark"></span>Verdant Ridge Inc.</div>
  <h2 class="header-title">Header 1</h2>
  <ul class="bullets"><li>Click to add text</li><li>Click to add text</li><li>Click to add text</li></ul>
  <div class="footer-band"></div>
</section>

<!-- Row 2 -->
<section class="slide col1 row2" aria-label="Title and two content slide">
  <div class="brand brand--small"><span class="brand__mark"></span>Verdant Ridge Inc.</div>
  <div class="ph ph--title" style="left:10px;top:24px;width:110px;height:20px">Click to add Title</div>
  <div class="ph" style="left:10px;top:48px;width:110px;height:128px">Click to add text</div>
  <div class="ph" style="left:128px;top:24px;width:107px;height:72px">Click to add text</div>
  <div class="ph" style="left:128px;top:102px;width:107px;height:74px">Click to add text</div>
  <div class="footer-band"></div>
</section>

<section class="slide col2 row2" aria-label="Content with caption slide">
  <div class="brand brand--small"><span class="brand__mark"></span>Verdant Ridge Inc.</div>
  <div class="ph ph--title" style="left:10px;top:24px;width:110px;height:20px">Click to add Title</div>
  <div class="ph" style="left:10px;top:48px;width:110px;height:128px">Click to add text</div>
  <div class="ph" style="left:128px;top:24px;width:107px;height:60px">Click to add text</div>
  <div class="ph" style="left:128px;top:90px;width:107px;height:86px">Click to add text</div>
  <div class="footer-band"></div>
</section>

<section class="slide col3 row2" aria-label="Title and content slide">
  <div class="brand brand--small"><span class="brand__mark"></span>Verdant Ridge Inc.</div>
  <div class="ph ph--title" style="left:10px;top:24px;width:225px;height:50px">Click to add text</div>
  <div class="ph" style="left:10px;top:80px;width:225px;height:36px">Click to add text</div>
  <div class="ph" style="left:10px;top:122px;width:225px;height:54px">Click to add text</div>
  <div class="footer-band"></div>
</section>

<section class="slide col4 row2" aria-label="Divider slide">
  <div class="brand brand--center" style="top:66px"><span class="brand__mark"></span>Verdant Ridge Inc.</div>
  <div class="ph ph--title ph--center divider-label">Divider Page</div>
  <div class="footer-band"></div>
</section>

<!-- Row 3 -->
<section class="slide col1 row3" aria-label="Comparison slide">
  <div class="brand brand--small"><span class="brand__mark"></span>Verdant Ridge Inc.</div>
  <div class="ph ph--title ph--center" style="left:10px;top:24px;width:225px;height:22px">Click to add Title</div>
  <div class="ph" style="left:10px;top:52px;width:110px;height:124px">Click to add text</div>
  <div class="ph" style="left:128px;top:52px;width:107px;height:60px">Click to add text</div>
  <div class="ph" style="left:128px;top:118px;width:107px;height:58px">Click to add text</div>
  <div class="footer-band"></div>
</section>

<section class="slide col2 row3" aria-label="Picture with caption slide">
  <div class="brand brand--small"><span class="brand__mark"></span>Verdant Ridge Inc.</div>
  <div class="ph ph--title" style="left:10px;top:60px;width:105px;height:22px">Click to add Title</div>
  <div class="ph" style="left:10px;top:86px;width:105px;height:90px">Click to add text</div>
  <div class="ph" style="left:124px;top:24px;width:111px;height:70px">Click to add text</div>
  <div class="ph" style="left:124px;top:100px;width:111px;height:76px">Click to add text</div>
  <div class="footer-band"></div>
</section>

<section class="slide col3 row3" aria-label="Title only slide">
  <div class="brand brand--small"><span class="brand__mark"></span>Verdant Ridge Inc.</div>
  <div class="ph" style="left:10px;top:24px;width:225px;height:80px">Click to add text</div>
  <div class="ph" style="left:10px;top:110px;width:225px;height:30px">Click to add text</div>
  <div class="ph" style="left:10px;top:146px;width:225px;height:30px">Click to add text</div>
  <div class="footer-band"></div>
</section>

<section class="slide slide--blue col4 row3" aria-label="Closing slide, blue">
  <div class="brand brand--center" style="top:92px"><span class="brand__mark"></span>Verdant Ridge Inc.</div>
</section>

</body>
</html>
```